EPC Marketing Flyer Pinefold HC

Company Name: Pinefold Homecheck Ltd
Product: Residential EPCs
Territory: Nationwide (UK)
Marketing channel: Flyer will be used for email and postal mailshots. We have not targeted this particular segment of the market before, so we need it to be eye catching, clearly messaged and encourage the recipient to get in touch.

We need a flyer to promote our services to conduct EPCs owned by public and private sector for residential ONLY (NOT Commercial), on a large or small scale.

Our Surveyors: experienced and accredited surveyors, quality service, quick and professional

Our Business: Warm Ledger Accredited, Reputation in business for excellence, fast growing

Our Service: Friendly, high quality, quick and professional

Colours: Designs in green and white (same shade as corporate colours), with our logo, and warm ledger accreditation logo, promoting our business.

Target Market(s)

Estate Agencies, Housing Associations, Local Authorities (Housing Departments), House Builders (NOT Home Owners Directly)

Industry/Entity Type

It Company

Font styles to use
Sans Serif
Other font styles liked:
• Calibri

Colors
add136
9bcb3c
cadf82
f6faec
eaf2ce

Requirements
Must have
• Our contact number etc must be clearly visible, and that we do EPCs
• Must state: What is an EPC? An EPC (Energy Performance Certificate) gives a property an energy efficiency rating from A (most efficient) to G (least efficient) and is valid for 10 years. An EPC can also provide recommendations on home improvement measures which once complete can improve the energy efficiency of the property.
• Who needs and EPC? All landlords and home owners, as all properties available to buy or rent require a valid and current EPC.
• Contact details:
• Tel: 08000 915 462
• Website: www.pinefold-hc.co.uk
• Email: epc@pinefold-hc.co.uk
• we must also be ably to print out the flyer
Nice to have
• Nice images to accompany the text which give a feeling of Environmentally Green, Home Energy Efficiency, Home Warmth and family - see example attached. And image of survey professional at work.
Should not have
• Any reference to cost or pricing
• Warm ledger logo art work must not be any other size that that specified in guidance document attached.

```html
<!DOCTYPE html>
<html lang="en">
<head>
<meta charset="utf-8">
<title>Pinefold Homecheck Ltd – EPC Flyer</title>
<link rel="stylesheet" href="https://fonts.googleapis.com/css2?family=PT+Sans:ital,wght@0,400;0,700;1,400;1,700&family=PT+Sans+Narrow:wght@700&display=swap">
<style>
  :root {
    --green: #9bcb3c;
    --green-deep: #1e9e4a;
    --green-head: #8dc63f;
    --pale: #f6faec;
    --pale-2: #eaf2ce;
    --ink: #2b1a10;
    --tag: #3a3a3a;
    --white: #ffffff;
    --black: #000000;
    --backdrop: #4a2c1e;
  }
  * { box-sizing: border-box; margin: 0; padding: 0; }
  html, body { width: 1200px; height: 857px; overflow: hidden; background: var(--backdrop); }
  body { position: relative; font-family: "PT Sans", Arial, sans-serif; }

  .flyer {
    position: absolute; left: 310px; top: 20px;
    width: 623px; height: 878px;
    transform: scale(0.93); transform-origin: top left;
    background: var(--white); overflow: hidden;
  }
  .top-band { position: absolute; left: 0; top: 0; width: 623px; height: 22px; background: var(--green); }
  .top-band .pale-block { position: absolute; left: 18px; top: 0; width: 323px; height: 22px; background: var(--pale); }

  .header { position: absolute; left: 0; top: 22px; width: 623px; height: 105px; background: var(--white); }
  .brand { position: absolute; left: 56px; top: 14px; display: flex; align-items: center; gap: 12px; }
  .brand-dot { width: 62px; height: 62px; border-radius: 50%; background: var(--green); flex: none; }
  .brand-name { font-size: 23px; font-weight: 700; color: var(--green-deep); line-height: 1.05; width: 170px; }
  .tagline { position: absolute; left: 358px; top: 36px; font-size: 13.5px; font-weight: 700; font-style: italic; color: var(--tag); line-height: 17px; }
  .tagline .accent { color: var(--green-deep); }

  .photo-fade { position: absolute; left: 0; top: 127px; width: 341px; height: 618px;
    background: linear-gradient(180deg, #e9ece4 0%, #dfe3d6 50%, #d8d4c6 100%); }
  .photo-family { position: absolute; left: 341px; top: 127px; width: 282px; height: 618px;
    background: linear-gradient(160deg, #e7e1d6 0%, #d27a3e 22%, #6b5a48 45%, #c39a7a 65%, #4f5563 100%); }

  .headline { position: absolute; left: 46px; top: 134px; font-family: "PT Sans Narrow", "Arial Narrow", sans-serif;
    font-size: 55px; line-height: 60px; color: var(--green-head); font-weight: 700; }
  .sub-headline { position: absolute; left: 47px; top: 368px; font-size: 21px; line-height: 23px; font-weight: 700; color: var(--ink); }

  .footer { position: absolute; left: 0; top: 745px; width: 623px; height: 133px; background: var(--black); border-top: 2px solid var(--white); }
  .contact-line { position: absolute; left: 43px; top: 42px; white-space: nowrap; color: var(--green); }
  .contact-line .label, .contact-line .or { font-size: 28px; }
  .contact-line .phone { font-size: 28px; font-weight: 700; margin: 0 4px 0 10px; }
  .contact-line .email { font-size: 18px; letter-spacing: 0.5px; margin-left: 6px; }
  .website { position: absolute; left: 0; width: 623px; top: 93px; text-align: center; color: var(--white); font-size: 14px; letter-spacing: 5.2px; }

  .shapes { position: absolute; left: 0; top: 0; width: 623px; height: 878px; }

  .epc-what { position: absolute; left: 45px; top: 482px; width: 235px; color: var(--white); }
  .epc-what h2 { font-size: 44px; font-weight: 700; line-height: 52px; }
  .epc-what h2 small { font-size: 16px; }
  .epc-what p { font-size: 14px; line-height: 17.5px; }

  .epc-who { position: absolute; left: 303px; top: 615px; width: 200px; color: var(--white); }
  .epc-who h2 { font-size: 22px; line-height: 22px; font-weight: 700; }
  .epc-who h3 { font-size: 16px; line-height: 18px; font-weight: 700; margin-bottom: 6px; }
  .epc-who p { font-size: 14px; line-height: 17.5px; }
</style>
</head>
<body>
<main class="flyer">
  <div class="top-band"><div class="pale-block"></div></div>

  <header class="header">
    <div class="brand">
      <span class="brand-dot"></span>
      <span class="brand-name">Pinefold Homecheck Ltd</span>
    </div>
    <p class="tagline"><span class="accent">Warm Ledger Accredited,</span> Reputation<br>in business for excellence, fast growing</p>
  </header>

  <div class="photo-fade" role="img" aria-label="Faded autumn woodland backdrop"></div>
  <div class="photo-family" role="img" aria-label="Family embracing outdoors among autumn trees"></div>

  <h1 class="headline">Friendly,<br>High Quality,<br>Quick and<br>Professional</h1>
  <p class="sub-headline">EXPERIENCED AND<br>ACCREDITED SURVEYORS</p>

  <footer class="footer">
    <p class="contact-line"><span class="label">Call Us</span><span class="phone">08000 915 462</span><span class="or">or</span><span class="email">epc@pinefold-hc.co.uk</span></p>
    <p class="website">www.pinefold-hc.co.uk</p>
  </footer>

  <svg class="shapes" viewBox="0 0 623 878" aria-hidden="false">
    <defs>
      <radialGradient id="house-tones" cx="50%" cy="45%" r="60%">
        <stop offset="0%" stop-color="#3f6b4a"/>
        <stop offset="55%" stop-color="#c9b79a"/>
        <stop offset="100%" stop-color="#f3efe6"/>
      </radialGradient>
    </defs>
    <circle cx="146" cy="601" r="176" fill="#9bcb3c"/>
    <circle cx="393" cy="658" r="119" fill="#1e9e4a" stroke="#ffffff" stroke-width="3"/>
    <g role="img" aria-label="Model house standing on a pile of coins">
      <circle cx="354" cy="536" r="70" fill="url(#house-tones)" stroke="#ffffff" stroke-width="3"/>
    </g>
  </svg>

  <section class="epc-what">
    <h2>What is <small>an EPC?</small></h2>
    <p>An EPC<br>(Energy Performance Certificate) gives a property an energy efficiency rating from A (most efficient) to G (least efficient) and is valid for 10 years. An EPC can also provide recommendations on home improvement measures which once complete can improve the energy efficiency of the property.</p>
  </section>

  <section class="epc-who">
    <h2>Who needs</h2>
    <h3>and EPC?</h3>
    <p>All landlords and home owners, as all properties available to buy or rent require a valid and current EPC.</p>
  </section>
</main>
</body>
</html>
```